BrivoPeak Business Card Design Project

We are looking for a modern, clean business card design for our new company. We are a consulting firm focused on the financial services market providing management and IT consulting to banks, insurance companies, etc. Please include our company logo and company contact information from the attached file in the design. Two versions of the logo are attached, either version is acceptable. Logos are available in other file formats if needed. We would like to include the contact information for both our UK and US offices as well as the following information for each individual card holder: Name, position/title, address, phone number and e-mail address.
Updates
Project Deadline Extended
Reason: A last minute trip over seas has prevented us from finalizing the decision. A decision will be made this week. We apologize for the inconvenience.
Industry/Entity Type
Business
Contact Information for Business Card
Company logo.
Company locations and phone numbers for both the US and UK offices.
Company URL.
Cardholder Name
Cardholder Position/title
Cardholder Address
Cardholder Phone Number
Cardholder e-mail Address
Look and feel
Each slider illustrates characteristics of the customer's brand and the style your logo design should communicate.

```html
<!DOCTYPE html>
<html lang="en">
<head>
<meta charset="utf-8">
<title>BrivoPeak Partners – Business Card</title>
<link rel="stylesheet" href="https://fonts.googleapis.com/css2?family=Mulish:ital,wght@0,400;0,700;1,400;1,700;1,800&display=swap">
<style>
  :root {
    --stage: #1f1f20;
    --card-top: #a9a9aa;
    --card-bottom: #4b4b4c;
    --band-light: #e4e4e6;
    --band-shade: #c9c9cc;
    --navy: #1d2a44;
    --brand-blue: #2f4d80;
    --ink: #111111;
    --ink-soft: #1c1c1c;
    --header-white: #f0f0f2;
  }
  * { margin: 0; padding: 0; box-sizing: border-box; }
  html, body {
    width: 1200px; height: 675px; overflow: hidden;
    background: var(--stage);
    font-family: "Mulish", "Helvetica Neue", Arial, sans-serif;
    color: var(--ink);
  }
  .stage { position: relative; width: 1200px; height: 675px; }
  .card {
    position: absolute; left: 339px; width: 556px; height: 266px;
    background: linear-gradient(to bottom, var(--card-top) 0%, #7d7d7e 45%, var(--card-bottom) 100%);
    overflow: hidden;
  }
  .card--back { top: 48px; }
  .card--front { top: 362px; }
  .card-band { position: absolute; left: 0; bottom: 0; width: 556px; height: 40px; }

  /* Back side */
  .addresses-title {
    position: absolute; top: 16px; left: 0; width: 100%;
    text-align: center; font-style: italic; font-weight: 800; font-size: 17px;
  }
  .office {
    position: absolute; top: 63px; width: 200px; text-align: center;
    font-style: italic; font-size: 13.2px; line-height: 23px; color: var(--ink-soft);
  }
  .office--us { left: 78px; }
  .office--uk { left: 308px; }
  .phones { position: absolute; left: 24px; top: 219px; font-style: italic; }
  .phones-title { font-weight: 800; font-size: 11.5px; }
  .phones-row { display: flex; font-size: 9px; line-height: 15px; color: #222; }
  .phones-row span:first-child { width: 58px; padding-left: 15px; }
  .web {
    position: absolute; right: 82px; bottom: 8px;
    font-style: italic; font-weight: 800; font-size: 14px;
  }

  /* Front side */
  .brand-header {
    position: absolute; top: 0; left: 0; width: 100%; height: 90px;
    background: linear-gradient(to bottom, #f6f6f7, #e6e6e8);
    display: flex; align-items: center; justify-content: center; gap: 12px;
  }
  .brand-mark { width: 22px; height: 22px; background: var(--brand-blue); }
  .brand-name { font-weight: 700; font-size: 30px; color: var(--brand-blue); letter-spacing: 0.2px; }
  .holder { position: absolute; left: 26px; top: 148px; display: flex; gap: 12px; align-items: center; }
  .holder-name { font-style: italic; font-weight: 800; font-size: 15px; letter-spacing: 0.3px; }
  .holder-title { font-style: italic; font-size: 11.5px; color: #222; margin-top: -2px; }
  .contact { position: absolute; left: 323px; font-style: italic; font-size: 12.8px; display: flex; align-items: center; gap: 5px; }
  .contact--phone { top: 143px; }
  .contact--mail { top: 170px; }
  .holder-address {
    position: absolute; left: 212px; bottom: 10px;
    font-style: italic; font-size: 14px; display: flex; align-items: center; gap: 7px;
  }
</style>
</head>
<body>
<main class="stage">

  <section class="card card--back" aria-label="Business card, company side">
    <h2 class="addresses-title">Company Addresses:</h2>
    <p class="office office--us">418 N Cedarline Ave, Suite<br>204-210<br>Maplewood UT 84920<br>United States</p>
    <p class="office office--uk">14-16 Harlow Street<br>London<br>E2 9QX<br>Great Britain</p>
    <div class="phones">
      <p class="phones-title">Company Phone Numbers:</p>
      <p class="phones-row"><span>US</span><span>(555) 214-7730</span></p>
      <p class="phones-row"><span>UK</span><span>+44 7700 900418</span></p>
    </div>
    <svg class="card-band" viewBox="0 0 556 40" aria-hidden="true">
      <defs>
        <linearGradient id="band-back" x1="0" y1="0" x2="0" y2="1">
          <stop offset="0" stop-color="#efeff1"/><stop offset="1" stop-color="#c6c6c9"/>
        </linearGradient>
      </defs>
      <rect x="0" y="35" width="190" height="5" fill="#1d2a44"/>
      <path d="M175 40 C190 18 205 4 240 4 L556 4 L556 40 Z" fill="url(#band-back)"/>
    </svg>
    <p class="web">www.brivopeakpartners.com</p>
  </section>

  <section class="card card--front" aria-label="Business card, cardholder side">
    <header class="brand-header">
      <span class="brand-mark"></span>
      <span class="brand-name">BrivoPeak Partners</span>
    </header>
    <div class="holder">
      <svg width="28" height="28" viewBox="0 0 28 28" aria-hidden="true">
        <circle cx="14" cy="14" r="14" fill="#111"/>
        <circle cx="14" cy="11" r="5" fill="#8a8a8b"/>
        <path d="M5 23 C7 17 21 17 23 23 A12 12 0 0 1 5 23 Z" fill="#8a8a8b"/>
      </svg>
      <div>
        <p class="holder-name">CARDHOLDER NAME</p>
        <p class="holder-title">Cardholder Position/title</p>
      </div>
    </div>
    <p class="contact contact--phone">
      <svg width="8" height="14" viewBox="0 0 8 14" aria-hidden="true"><rect x="0.7" y="0.7" width="6.6" height="12.6" rx="1.2" fill="none" stroke="#111" stroke-width="1.4"/><rect x="3" y="11" width="2" height="1" fill="#111"/></svg>
      Cardholder Phone Number
    </p>
    <p class="contact contact--mail">
      <svg width="12" height="10" viewBox="0 0 12 10" aria-hidden="true"><path d="M0 4 L6 0 L12 4 L12 10 L0 10 Z" fill="#111"/><path d="M1 4.5 L6 7.5 L11 4.5" fill="none" stroke="#8a8a8b" stroke-width="1"/></svg>
      Cardholder e-mail Address
    </p>
    <svg class="card-band" viewBox="0 0 556 40" aria-hidden="true">
      <defs>
        <linearGradient id="band-front" x1="0" y1="0" x2="0" y2="1">
          <stop offset="0" stop-color="#efeff1"/><stop offset="1" stop-color="#c6c6c9"/>
        </linearGradient>
      </defs>
      <rect x="0" y="32" width="190" height="8" fill="#1d2a44"/>
      <path d="M175 40 C190 14 205 0 240 0 L556 0 L556 40 Z" fill="url(#band-front)"/>
    </svg>
    <p class="holder-address">
      <svg width="26" height="22" viewBox="0 0 26 22" aria-hidden="true">
        <path d="M1 14 L9 12 L17 14 L25 12 L25 21 L17 22 L9 20 L1 22 Z" fill="#111"/>
        <path d="M15 0 A5 5 0 0 1 20 5 C20 9 15 13 15 13 C15 13 10 9 10 5 A5 5 0 0 1 15 0 Z" fill="#111"/>
        <circle cx="15" cy="5" r="2" fill="#e4e4e6"/>
      </svg>
      Cardholder Address
    </p>
  </section>

</main>
</body>
</html>
```